RK Bastone Construction Inc.

Design a new business card for our construction company
To be removed from current card:
Delete 25 years
Delete Tenant fit up Renovations section

```html
<!DOCTYPE html>
<html lang="en">
<head>
<meta charset="utf-8">
<title>RK Bastone Construction Inc. — Business Card</title>
<link rel="stylesheet" href="https://fonts.googleapis.com/css2?family=Montserrat:wght@400;500;700;800&display=swap">
<style>
  :root {
    --purple: #5b2d7f;
    --purple-deep: #4a2268;
    --teal: #1f7a6c;
    --ink: #2b2b2b;
    --paper: #ffffff;
    --stage: #2a2a2c;
    --rule: #8a6aa3;
  }
  * { box-sizing: border-box; margin: 0; padding: 0; }
  html, body {
    width: 1200px; height: 900px; overflow: hidden;
    background: var(--stage);
    font-family: "Montserrat", sans-serif;
  }
  .sheet {
    position: relative; width: 1200px; height: 900px;
    display: flex; flex-direction: column; align-items: center; justify-content: center; gap: 56px;
  }
  .card {
    position: relative; width: 640px; height: 366px;
    border-radius: 16px; overflow: hidden;
  }
  /* Back side */
  .card-back {
    background: var(--purple);
    display: flex; flex-direction: column; align-items: center; justify-content: center;
    color: var(--paper);
  }
  .wordmark { font-weight: 700; text-transform: uppercase; line-height: 1; }
  .card-back .wordmark { text-align: left; }
  .card-back .wordmark-main { font-size: 62px; letter-spacing: 0.5px; display: block; }
  .card-back .wordmark-sub { font-size: 24px; letter-spacing: 5.2px; display: block; margin-top: 8px; }
  .services {
    margin-top: 44px; font-size: 15px; font-weight: 500; letter-spacing: 1.2px;
  }
  .services .sep { margin: 0 12px; }
  /* Front side */
  .card-front { background: var(--paper); }
  .card-front .wordmark {
    position: absolute; left: 44px; top: 138px; color: var(--purple);
  }
  .card-front .wordmark-main { font-size: 34px; display: block; }
  .card-front .wordmark-sub { font-size: 13px; letter-spacing: 2.9px; display: block; margin-top: 5px; }
  .divider {
    position: absolute; left: 300px; top: 70px; width: 1px; height: 200px; background: var(--rule);
  }
  .contact { position: absolute; left: 326px; top: 62px; color: var(--ink); }
  .person-name { font-size: 25px; font-weight: 800; letter-spacing: 0.5px; line-height: 1; }
  .person-name .first { color: var(--purple); }
  .person-name .last { color: var(--teal); }
  .person-role { font-size: 13px; font-weight: 500; margin-top: 3px; }
  .address { font-size: 14px; font-weight: 500; line-height: 1.35; margin-top: 14px; }
  .lines { list-style: none; margin-top: 12px; font-size: 14px; font-weight: 500; line-height: 1.55; }
  .lines li { display: flex; align-items: center; gap: 8px; }
  .lines svg { width: 11px; height: 11px; flex: none; fill: var(--teal); }
  .lines .web .domain { color: var(--teal); }
  .edge { position: absolute; left: 0; bottom: 0; width: 640px; height: 44px; }
</style>
</head>
<body>
<main class="sheet">
  <section class="card card-back" aria-label="Card back">
    <div class="wordmark">
      <span class="wordmark-main">RK Bastone</span>
      <span class="wordmark-sub">Construction Inc.</span>
    </div>
    <p class="services">Office<span class="sep">|</span>Retail<span class="sep">|</span>Institutional</p>
  </section>

  <section class="card card-front" aria-label="Card front">
    <div class="wordmark">
      <span class="wordmark-main">RK Bastone</span>
      <span class="wordmark-sub">Construction Inc.</span>
    </div>
    <div class="divider"></div>
    <div class="contact">
      <h1 class="person-name"><span class="first">MARCO</span> <span class="last">BASTONE</span></h1>
      <p class="person-role">President</p>
      <p class="address">2180 Ridgeline Ave., Unit 4B<br>Barrie, ON L4M 2T8</p>
      <ul class="lines">
        <li><svg viewBox="0 0 12 12"><path d="M2.5 1l2 2.2-1 1.3a7 7 0 0 0 4 4l1.3-1L11 9.5 9.6 11C5 11 1 7 1 2.4z"/></svg><span>705-555-0148</span></li>
        <li><svg viewBox="0 0 12 12"><path d="M3 0h6a1 1 0 0 1 1 1v10a1 1 0 0 1-1 1H3a1 1 0 0 1-1-1V1a1 1 0 0 1 1-1zm.5 1.5v8h5v-8z"/></svg><span>705-555-0192 ext. 37</span></li>
        <li><svg viewBox="0 0 12 12"><path d="M0 2h12v8H0zm1.2 1.2v.3L6 6.6l4.8-3.1v-.3z"/></svg><span>marco@rkbastoneconst.ca</span></li>
        <li class="web"><svg viewBox="0 0 12 12"><path d="M6 0a6 6 0 1 0 0 12A6 6 0 0 0 6 0zm0 1.2c.8.7 1.4 2 1.6 3.8H4.4C4.6 3.2 5.2 1.9 6 1.2zM1.3 6.2h2c.1 1.6.5 3 1.1 4A4.8 4.8 0 0 1 1.3 6.2zm0-1.2a4.8 4.8 0 0 1 3.1-3.2C3.8 2.7 3.4 3.8 3.3 5zm4.7 5.8C5.2 10 4.6 8.4 4.4 6.2h3.2C7.4 8.4 6.8 10 6 10.8zm1.6-.6c.6-1 1-2.4 1.1-4h2a4.8 4.8 0 0 1-3.1 4zM8.7 5c-.1-1.2-.5-2.3-1.1-3.2A4.8 4.8 0 0 1 10.7 5z"/></svg><span>www.<span class="domain">rkbastoneconstruction.ca</span></span></li>
      </ul>
    </div>
    <svg class="edge" viewBox="0 0 640 44" preserveAspectRatio="none" aria-hidden="true">
      <polygon points="0,30 568,16 556,44 0,44" fill="var(--purple)"/>
      <polygon points="576,16 640,2 640,44 564,44" fill="var(--teal)"/>
    </svg>
  </section>
</main>
</body>
</html>
```